Chicken Coop Sign

I would like to make a metal chicken coop sign in the size of 8 x 12 inches. The orientation can be vertical or horizontal.

I would like the designer to use any of these funny phrases and try and create a catchy graphic based on some of the designs that are already in the market.

"The Poultry Palace: Where Every Hen is a Queen"

"The Hen Den: No Foxes Allowed"

"The Eggsecutive Mansion"

"The Cluck Hut: No Fowl Moods Allowed"

"The Cluck and Fluff: Luxury Lodging for Hens"

Families that have chicken coops as a hobby in their backyard or farm.

• It must be funny, use one of the provided quotes, have a "vintage" or "rustic" look
• Stay away from 4 letter words like "SHIT", "FUCK" or Starred out works like "S**T" and "F**K"

```html
<!DOCTYPE html>
<html lang="en">
<head>
<meta charset="utf-8">
<title>The Poultry Palace – Coop Sign</title>
<link rel="stylesheet" href="https://fonts.googleapis.com/css2?family=Abril+Fatface&family=Alegreya+Sans+SC:wght@800&display=swap">
<style>
  :root {
    --page: #ffffff;
    --plate: #efeedb;
    --edge: #141414;
    --green: #21513a;
    --gold: #c89a3c;
    --ink: #1a1a1a;
    --coop-a: #dfe6f2;
    --coop-b: #6f9a45;
    --hen-a: #f3ead8;
    --hen-b: #d9c4a4;
  }
  * { margin: 0; padding: 0; box-sizing: border-box; }
  html, body {
    width: 1200px; height: 1145px; overflow: hidden;
    background: var(--page);
  }
  .canvas { position: relative; width: 1200px; height: 1145px; }

  .sign {
    position: absolute; left: 272px; top: 87px;
    width: 668px; height: 969px;
    background: var(--plate);
    border-radius: 14px;
    box-shadow: 0 6px 14px rgba(0,0,0,0.18);
    overflow: hidden;
  }
  .sign-frame { position: absolute; inset: 0; }

  .screw-hole {
    position: absolute; width: 22px; height: 22px;
    border-radius: 50%; background: var(--page);
    border: 2px solid #888;
  }
  .screw-hole.tl { left: 14px; top: 14px; }
  .screw-hole.tr { right: 14px; top: 14px; }
  .screw-hole.bl { left: 14px; bottom: 14px; }
  .screw-hole.br { right: 14px; bottom: 14px; }

  .coop-art {
    position: absolute; left: 47px; top: 88px;
    width: 356px; height: 325px;
    border-radius: 24px;
    background: linear-gradient(160deg, var(--coop-a) 0%, var(--coop-a) 45%, var(--coop-b) 100%);
  }
  .hen-art {
    position: absolute; left: 284px; top: 32px;
    width: 344px; height: 500px;
    border-radius: 48% 48% 40% 40%;
    background: radial-gradient(ellipse at 50% 40%, var(--hen-a) 0%, var(--hen-b) 100%);
  }

  .title {
    position: absolute; left: 0; width: 100%;
    font-family: "Abril Fatface", serif;
    color: var(--green);
    text-shadow: 4px 4px 0 var(--gold);
    line-height: 1;
    white-space: nowrap;
  }
  .title-the { top: 420px; left: 95px; width: auto; font-size: 118px; }
  .title-poultry { top: 522px; text-align: center; font-size: 150px; letter-spacing: -2px; }
  .title-palace { top: 638px; left: 150px; width: auto; font-size: 140px; letter-spacing: -2px; }

  .tagline {
    position: absolute; left: 0; width: 100%; top: 806px;
    text-align: center;
    font-family: "Alegreya Sans SC", sans-serif;
    font-weight: 800;
    font-size: 42px;
    color: var(--ink);
    letter-spacing: 0.5px;
  }

  .flourish {
    position: absolute; left: 247px; top: 886px;
    width: 176px; height: 26px;
    border-radius: 13px;
    background: var(--gold);
  }
</style>
</head>
<body>
<div class="canvas">
  <div class="sign">
    <svg class="sign-frame" width="668" height="969" viewBox="0 0 668 969" aria-hidden="true">
      <rect x="6" y="6" width="656" height="957" rx="12" fill="none" stroke="var(--edge)" stroke-width="14"/>
      <rect x="24" y="24" width="620" height="921" rx="6" fill="none" stroke="var(--edge)" stroke-width="2" opacity="0.5"/>
    </svg>

    <div class="coop-art" role="img" aria-label="Illustration of a white wooden chicken coop on green grass"></div>
    <div class="hen-art" role="img" aria-label="Illustration of a white hen wearing a golden crown"></div>

    <div class="title title-the">The</div>
    <div class="title title-poultry">Poultry</div>
    <div class="title title-palace">Palace</div>

    <div class="tagline">Where Every Hen is a Queen</div>

    <div class="flourish" role="img" aria-label="Small gold scroll ornament"></div>

    <span class="screw-hole tl"></span>
    <span class="screw-hole tr"></span>
    <span class="screw-hole bl"></span>
    <span class="screw-hole br"></span>
  </div>
</div>
</body>
</html>
```